Calloway Holdings Website Design

We are a private equity firm based with offices based in Hong Kong, Singapore, London and Paris. Our focus is investments in property development projects, corporate ventures and loans.

We require the development of a new website and you will have to select relevant images from the likes of PixelVaultPics or other stock photo libraries.

We will need a design done for a PC based website and the designer selected with the favored design will also need to produce some concepts for a responsive website.

Target Market(s)

Sophisticated investors looking to invest in high return property development, businesses and mortgages.

Industry/Entity Type

Investment

Number of Pages Required

5+ page

Font styles to use
Serif
Sans Serif

Colors
0255a3
00a990

Requirements
Must have
• Clean modern feel and must portray stability and professionalism.

```html
<!DOCTYPE html>
<html lang="en">
<head>
<meta charset="utf-8">
<title>Calloway Holdings</title>
<link href="https://fonts.googleapis.com/css2?family=Raleway:wght@400;500;600;700&family=Arimo:wght@400;700&display=swap" rel="stylesheet">
<style>
:root{
  --blue:#0255a3;
  --navy:#0b3f8f;
  --teal:#00a990;
  --teal-dark:#00907b;
  --gold:#e9a91f;
  --ink:#333;
  --muted:#999;
  --light:#efeff1;
  --line:#e2e2e2;
  --badge:#b9b9b9;
  --white:#fff;
  --footer:#1d1d1d;
}
*{margin:0;padding:0;box-sizing:border-box}
html,body{width:1200px;height:3333px;overflow:hidden}
body{font-family:"Arimo",Arial,sans-serif;color:var(--ink);background:var(--white);position:relative}
h1,h2,h3,.nav,.source-label{font-family:"Raleway",Arial,sans-serif}
section,header,footer{position:absolute;left:0;width:1200px}

/* header */
.site-header{top:0;height:125px;background:var(--white)}
.brand{position:absolute;left:80px;top:44px;display:flex;align-items:center;gap:10px;font-family:"Raleway",sans-serif;font-weight:700;font-size:22px;color:var(--navy)}
.brand-dot{width:18px;height:18px;border-radius:50%;background:var(--teal)}
.nav{position:absolute;right:80px;top:52px;display:flex;gap:36px;font-size:16px;font-weight:500;color:var(--blue);letter-spacing:.2px}
.nav .active{color:var(--teal)}

/* hero */
.hero{top:125px;height:530px;background:linear-gradient(180deg,#eef3f8 0%,#d9e2ec 35%,#aab7c5 70%,#8d9aa8 100%)}
.hero-text{position:absolute;top:52px;width:100%;text-align:center}
.hero h1{font-size:64px;font-weight:700;color:var(--blue);letter-spacing:-.5px}
.hero h2{font-size:38px;font-weight:700;color:var(--blue);margin-top:6px}
.dots{position:absolute;top:490px;left:562px;display:flex;gap:14px}
.dots span{width:12px;height:12px;border-radius:50%;background:rgba(255,255,255,.6)}
.dots span:first-child{background:var(--white)}

/* who we are */
.who{top:655px;height:418px;background:var(--light)}
.who h2{position:absolute;left:78px;top:50px;font-size:40px;font-weight:500;color:var(--blue)}
.who h2 em,.section-title em{font-style:normal;color:var(--teal)}
.who p{position:absolute;left:78px;top:112px;width:515px;font-size:15px;line-height:22px;color:#555}
.btn-more{position:absolute;left:78px;top:303px;width:146px;height:50px;border-radius:25px;background:var(--blue);color:var(--white);font-size:15px;display:flex;align-items:center;justify-content:center}
.who-photo{position:absolute;left:612px;top:40px;width:510px;height:340px;background:radial-gradient(ellipse at 55% 50%,#c9a77a 0%,#9a9ca3 30%,#d7d8dc 62%,var(--light) 90%)}

/* services */
.services{top:1073px;height:552px}
.section-title{text-align:center;font-size:40px;font-weight:500;color:var(--blue)}
.services .section-title{margin-top:48px}
.service-list{position:absolute;top:130px;left:60px;display:flex}
.service{width:270px;text-align:center}
.service svg{display:block;margin:0 auto}
.service h3{font-size:17px;font-weight:500;color:#333;margin-top:26px;line-height:22px;height:46px}
.service p{font-size:15px;line-height:22px;color:var(--muted);margin:14px auto 0;width:225px}

/* sources */
.sources-band{top:1625px;height:103px;background:var(--blue)}
.sources-band h2{text-align:center;font-size:40px;font-weight:500;color:var(--white);line-height:103px}
.sources-band .notch{position:absolute;left:586px;bottom:-14px;border-left:14px solid transparent;border-right:14px solid transparent;border-top:14px solid var(--blue)}
.sources{top:1728px;height:657px;background:var(--teal)}
.sources svg.links{position:absolute;left:0;top:0}
.source-label{position:absolute;font-size:17px;font-weight:500;color:var(--white);text-align:center;width:300px}
.src-art{position:absolute;width:140px;height:140px;border-radius:50%;border:4px solid var(--white);background:var(--teal)}
.art-funds{background:radial-gradient(circle at 50% 50%,#f6c84a 0%,var(--gold) 38%,#18b39a 62%,var(--teal) 100%)}
.art-institution{background:radial-gradient(circle at 52% 48%,#e9f3f7 0%,#9fc4d6 38%,#2bb69f 66%,var(--teal) 100%)}
.art-advisors{background:radial-gradient(circle at 50% 58%,#3a3f47 0%,#5b5f66 34%,#1fb39b 64%,var(--teal) 100%)}
.art-strategic{background:radial-gradient(circle at 48% 52%,#f2c03c 0%,#d99a18 30%,#26b69c 62%,var(--teal) 100%)}
.art-hnw{background:radial-gradient(circle at 50% 52%,#f1bc3a 0%,#4f8fd0 38%,#22b49c 64%,var(--teal) 100%)}
.hub{position:absolute;left:450px;top:222px;width:300px;height:96px;display:flex;align-items:center;justify-content:center;gap:12px;font-family:"Raleway",sans-serif;font-weight:700;font-size:32px;color:var(--navy)}
.hub .dot{width:30px;height:30px;border-radius:50%;background:var(--navy)}

/* partners */
.partners{top:2385px;height:330px}
.partners .section-title{margin-top:44px}
.partner-grid{position:absolute;top:112px;left:100px;display:grid;grid-template-columns:repeat(6,167px);grid-template-rows:repeat(2,92px)}
.partner{display:flex;align-items:center;justify-content:center;border-right:1px solid var(--line);border-bottom:1px solid var(--line)}
.partner:nth-child(6n){border-right:none}
.partner:nth-child(n+7){border-bottom:none}
.badge{display:block;background:var(--badge)}
.b-wide{width:118px;height:30px;border-radius:3px}
.b-mid{width:94px;height:34px;border-radius:3px}
.b-pill{width:82px;height:34px;border-radius:17px}
.b-square{width:40px;height:40px;border-radius:4px}
.b-circle{width:44px;height:44px;border-radius:50%}
.b-red{background:#e0454a;width:84px;height:34px;border-radius:3px}
.b-dark{background:#8c8c8c}

/* quote */
.quote{top:2715px;height:555px}
.quote-form{position:absolute;left:0;top:0;width:625px;height:555px;background:linear-gradient(180deg,#1f66b8,#0d57a8)}
.quote-form h2{position:absolute;left:0;width:625px;text-align:center;top:52px;font-size:40px;font-weight:500;color:var(--white);letter-spacing:.5px}
.field{position:absolute;left:78px;width:500px;border:2px solid rgba(255,255,255,.55);color:rgba(255,255,255,.85);font-size:15px;padding:13px 20px}
.f-name{top:166px;height:52px;color:var(--white)}
.f-mail{top:229px;height:52px}
.f-msg{top:292px;height:126px}
.submit{position:absolute;left:78px;top:428px;width:500px;height:52px;border-radius:26px;background:var(--teal);color:var(--white);font-weight:700;font-size:20px;display:flex;align-items:center;justify-content:center;letter-spacing:.5px}
.map{position:absolute;left:625px;top:0;width:575px;height:555px;background:linear-gradient(135deg,#e9e4da,#ddd7cc)}
.offices{position:absolute;left:838px;top:116px;width:282px;height:326px;background:var(--blue);color:var(--white);padding:20px 22px;list-style:none}
.offices li{margin-bottom:16px;font-size:18px;font-family:"Raleway",sans-serif}
.offices li::before{content:"• "}
.offices li.active{color:var(--teal)}
.offices .detail{font-size:14px;line-height:20px;margin-bottom:14px;font-family:"Arimo",sans-serif}
.offices .detail::before{content:none}

/* footer */
.site-footer{top:3270px;height:63px;background:var(--footer);color:#cfcfcf;font-size:13px}
.site-footer p{position:absolute;left:82px;top:24px}
.site-footer p span{color:var(--teal)}
.social{position:absolute;right:80px;top:24px;display:flex;gap:26px}
.social span{width:15px;height:15px;border-radius:50%;background:var(--teal)}
</style>
</head>
<body>

<header class="site-header">
  <div class="brand"><span class="brand-dot"></span>Calloway Holdings</div>
  <nav class="nav">
    <span class="active">HOME</span><span>SERVICES</span><span>INVESTMENT APPROACH</span><span>MISSIONS &amp; VALUES</span><span>CONTACT</span>
  </nav>
</header>

<section class="hero" role="img" aria-label="Aerial photograph of a city skyline of office towers under a pale sky">
  <div class="hero-text">
    <h1>YOU NEED VISIBILITY.</h1>
    <h2>We can help you see.</h2>
  </div>
  <div class="dots"><span></span><span></span><span></span></div>
</section>

<section class="who">
  <h2>WHO <em>WE ARE</em></h2>
  <p>Calloway Holdings is a is a boutique independent investment group that specializes in direct investments along with the provision of consulting and fund raising services to both established and emerging private companies. We are attracted to challenging assignments.<br>With significant years of combined industry experience and international presence.</p>
  <div class="btn-more">READ MORE</div>
  <div class="who-photo" role="img" aria-label="Photograph of business people meeting around a round table, seen from above"></div>
</section>

<section class="services">
  <h2 class="section-title">SERVICES <em>WE PROVIDE</em></h2>
  <div class="service-list">
    <div class="service">
      <svg width="170" height="200" viewBox="0 0 170 200"><circle cx="85" cy="100" r="78" fill="none" stroke="#0b3f8f" stroke-width="14"/><circle cx="85" cy="100" r="44" fill="#00a990"/><path d="M70 118v-30h30v30M78 88v-8h14v8" fill="none" stroke="#fff" stroke-width="4"/></svg>
      <h3>ANGEL INVESTMENT</h3>
      <p>Lorem Ipsum is simply dummy text of the printing and typesetting industry.</p>
    </div>
    <div class="service">
      <svg width="170" height="200" viewBox="0 0 170 200"><circle cx="85" cy="100" r="78" fill="none" stroke="#666" stroke-width="14"/><circle cx="85" cy="100" r="44" fill="#666"/><circle cx="85" cy="100" r="20" fill="none" stroke="#fff" stroke-width="4"/><text x="85" y="108" text-anchor="middle" font-family="Arimo,sans-serif" font-size="22" font-weight="700" fill="#fff">$</text></svg>
      <h3>CAPITAL RAISINGS</h3>
      <p>Lorem Ipsum is simply dummy text of the printing and typesetting industry.</p>
    </div>
    <div class="service">
      <svg width="170" height="200" viewBox="0 0 170 200"><circle cx="85" cy="100" r="78" fill="none" stroke="#666" stroke-width="14"/><circle cx="85" cy="100" r="44" fill="#666"/><path d="M58 100h54M66 92l-8 8 8 8M104 92l8 8-8 8" fill="none" stroke="#fff" stroke-width="4"/><text x="85" y="108" text-anchor="middle" font-family="Arimo,sans-serif" font-size="22" font-weight="700" fill="#fff">$</text></svg>
      <h3>MERGERS, ACQUISITIONS &amp; DIVESTMENTS</h3>
      <p>Lorem Ipsum is simply dummy text of the printing and typesetting industry.</p>
    </div>
    <div class="service">
      <svg width="170" height="200" viewBox="0 0 170 200"><circle cx="85" cy="100" r="78" fill="none" stroke="#666" stroke-width="14"/><circle cx="85" cy="100" r="44" fill="#666"/><g fill="none" stroke="#fff" stroke-width="3"><rect x="75" y="80" width="20" height="12"/><rect x="60" y="110" width="18" height="12"/><rect x="92" y="110" width="18" height="12"/><path d="M85 92v9M69 101h32M69 101v9M101 101v9"/></g></svg>
      <h3>CAPITAL &amp; CORPORATE RESTRUCTURE</h3>
      <p>Lorem Ipsum is simply dummy text of the printing and typesetting industry.</p>
    </div>
  </div>
</section>

<section class="sources-band"><h2>OUR SOURCES</h2><span class="notch"></span></section>

<section class="sources">
  <svg class="links" width="1200" height="657" viewBox="0 0 1200 657">
    <g fill="none" stroke="#fff" stroke-width="3">
      <path d="M312 218v52h138M890 218v52H750"/>
      <path d="M600 318v24M312 406v-64h578v64M600 342v64"/>
    </g>
  </svg>
  <div class="source-label" style="left:162px;top:40px">OUR OWN FUNDS</div>
  <div class="source-label" style="left:740px;top:40px">INSTITUTION INVESTORS</div>
  <div class="src-art art-funds" style="left:242px;top:74px" role="img" aria-label="Illustration of a gold piggy bank with coins"></div>
  <div class="src-art art-institution" style="left:820px;top:74px" role="img" aria-label="Illustration of a glass office building"></div>
  <div class="hub"><span class="dot"></span>Calloway</div>
  <div class="src-art art-advisors" style="left:242px;top:406px" role="img" aria-label="Illustration of a consultant in a dark suit"></div>
  <div class="src-art art-strategic" style="left:530px;top:406px" role="img" aria-label="Illustration of a gold dollar sign with a rising arrow"></div>
  <div class="src-art art-hnw" style="left:820px;top:406px" role="img" aria-label="Illustration of a gold dollar sign over stacked coins"></div>
  <div class="source-label" style="left:162px;top:580px">ADVISORS &amp; CONSULTANTS</div>
  <div class="source-label" style="left:450px;top:580px">STRATEGIC CORPORATE</div>
  <div class="source-label" style="left:740px;top:580px">HIGH NET-WORTH INDIVIDUALS</div>
</section>

<section class="partners">
  <h2 class="section-title">OUR <em>PARTNERS</em></h2>
  <div class="partner-grid" aria-label="Partner badges">
    <div class="partner"><span class="badge b-mid"></span></div>
    <div class="partner"><span class="badge b-wide b-dark"></span></div>
    <div class="partner"><span class="badge b-square"></span></div>
    <div class="partner"><span class="badge b-pill"></span></div>
    <div class="partner"><span class="badge b-red"></span></div>
    <div class="partner"><span class="badge b-wide"></span></div>
    <div class="partner"><span class="badge b-circle b-dark"></span></div>
    <div class="partner"><span class="badge b-pill"></span></div>
    <div class="partner"><span class="badge b-wide b-dark"></span></div>
    <div class="partner"><span class="badge b-circle"></span></div>
    <div class="partner"><span class="badge b-mid b-dark"></span></div>
    <div class="partner"><span class="badge b-square"></span></div>
  </div>
</section>

<section class="quote">
  <div class="quote-form">
    <h2>REQUEST A QUOTE</h2>
    <div class="field f-name">Name</div>
    <div class="field f-mail">E-Mail</div>
    <div class="field f-msg">Message</div>
    <div class="submit">SUBMIT</div>
  </div>
  <div class="map" role="img" aria-label="Street map showing the office location with a red pin"></div>
  <ul class="offices">
    <li>HONG KONG</li>
    <li class="active">LONDON</li>
    <li class="detail">Address : 48 Larkspur Quay, Harbourside, LN 40217</li>
    <li class="detail">Phone : (555) 310-4826</li>
    <li class="detail">E-Mail : hello@callowayholdings.example</li>
    <li>SINGAPORE</li>
    <li>PARIS</li>
  </ul>
</section>

<footer class="site-footer">
  <p>© <span>CALLOWAY HOLDINGS</span> 2016. All Rights Reserved</p>
  <div class="social" aria-label="Social links"><span></span><span></span><span></span><span></span></div>
</footer>

</body>
</html>
```